Boilerplate Management Organization Chart

"Our Management Approach is a deliberate step-by-step process and supports our Technical Approach detailed in proposal submission. The Management Approach covers all the human capital aspects for executing a contract—from contract award through to sustainment and/or transition of the contract to another company. It includes how we organize, hire, staff, train, and account for our contract employees—as well as their complete personal life-cycle management within the company."

We need this management approach to depict an amazing management process that demonstrates best practices of the project management body of knowledge. We need this vector image to be applicable to any proposal without making references to any other proposals. Generic names but using strong business language.
Updates

Thanks for all designs submitted thus far. Some have stuck to the original type of chart. We would like to see a completely different way to show the same information. It has to be able to be recognized and deciphered very quickly by people who might not necessarily want to look at it. It must draw them in and make it incredibly easy to distinguish a management approach that looks fresh, infallible, and easily implemented.

Target Market(s)

Federal space, Government organizations looking for procedural efficiencies,

Industry/Entity Type

Management

Requirements
Must have
• Must not take up more than 1/3 to 1/2 of printable page and be clear.
Should not have
• Not too much color, but should stick to some color palette of some interest.

```html
<!DOCTYPE html>
<html lang="en">
<head>
<meta charset="utf-8">
<title>Management Approach – Program Evaluation</title>
<link rel="stylesheet" href="https://fonts.googleapis.com/css2?family=Roboto+Condensed:wght@700;900&display=swap">
<style>
  :root {
    --page: #ffffff;
    --ink: #231f20;
    --ink-light: #ffffff;
    --seg-1: #bcbdbf;
    --seg-2: #a7a8ab;
    --seg-3: #939598;
    --seg-4: #808285;
    --seg-5: #6d6e71;
    --seg-6: #58595b;
    --seg-7: #414042;
    --seg-8: #231f20;
    --divider: #ffffff;
    --arrow-edge: rgba(35, 31, 32, 0.35);
  }
  html, body {
    margin: 0;
    padding: 0;
    width: 1200px;
    height: 1200px;
    overflow: hidden;
    background: var(--page);
  }
  .diagram {
    display: block;
    width: 1200px;
    height: 1200px;
  }
  .header-box { fill: var(--seg-1); stroke: #d1d2d4; stroke-width: 4; }
  .header-text {
    font-family: "Roboto Condensed", "Arial Narrow", sans-serif;
    font-weight: 900;
    font-size: 60px;
    fill: var(--ink);
    text-anchor: middle;
  }
  .pointer { fill: var(--seg-1); }
  .segment { stroke: var(--divider); stroke-width: 4; }
  .seg-1 { fill: var(--seg-1); }
  .seg-2 { fill: var(--seg-2); }
  .seg-3 { fill: var(--seg-3); }
  .seg-4 { fill: var(--seg-4); }
  .seg-5 { fill: var(--seg-5); }
  .seg-6 { fill: var(--seg-6); }
  .seg-7 { fill: var(--seg-7); }
  .seg-8 { fill: var(--seg-8); }
  .flow-arrow {
    stroke: var(--arrow-edge);
    stroke-width: 2;
    stroke-linejoin: round;
  }
  .step-label {
    font-family: "Roboto Condensed", "Arial Narrow", sans-serif;
    font-weight: 700;
    font-size: 33px;
    text-anchor: middle;
  }
  .step-label.dark { fill: var(--ink); }
  .step-label.light { fill: var(--ink-light); }
  .title {
    font-family: "Roboto Condensed", "Arial Narrow", sans-serif;
    font-weight: 900;
    font-size: 96px;
    fill: var(--ink);
    text-anchor: middle;
  }
</style>
</head>
<body>
<svg class="diagram" viewBox="0 0 1300 1300" xmlns="http://www.w3.org/2000/svg" aria-label="Management approach cycle leading to program evaluation">

  <g class="header">
    <rect class="header-box" x="602" y="77" width="441" height="148" rx="30"/>
    <text class="header-text" x="822" y="143">MANAGEMENT</text>
    <text class="header-text" x="822" y="211">APPROACH</text>
    <path class="pointer" d="M773 225 H787 V272 H800 L780 296 L760 272 H773 Z"/>
  </g>

  <g class="wheel">
    <path class="segment seg-1" d="M615 541 L615 270 A418 418 0 0 1 910.6 392.4 L718.9 584.1 A147 147 0 0 0 615 541 Z"/>
    <path class="segment seg-2" d="M718.9 584.1 L910.6 392.4 A418 418 0 0 1 1033 688 L762 688 A147 147 0 0 0 718.9 584.1 Z"/>
    <path class="segment seg-3" d="M762 688 L1033 688 A418 418 0 0 1 910.6 983.6 L718.9 791.9 A147 147 0 0 0 762 688 Z"/>
    <path class="segment seg-4" d="M718.9 791.9 L910.6 983.6 A418 418 0 0 1 615 1106 L615 835 A147 147 0 0 0 718.9 791.9 Z"/>
    <path class="segment seg-5" d="M615 835 L615 1106 A418 418 0 0 1 319.4 983.6 L511.1 791.9 A147 147 0 0 0 615 835 Z"/>
    <path class="segment seg-6" d="M511.1 791.9 L319.4 983.6 A418 418 0 0 1 197 688 L468 688 A147 147 0 0 0 511.1 791.9 Z"/>
    <path class="segment seg-7" d="M468 688 L197 688 A418 418 0 0 1 319.4 392.4 L511.1 584.1 A147 147 0 0 0 468 688 Z"/>
    <path class="segment seg-8" d="M511.1 584.1 L319.4 392.4 A418 418 0 0 1 615 270 L615 541 A147 147 0 0 0 511.1 584.1 Z"/>
  </g>

  <g class="flow-arrows" transform="translate(615 688)">
    <path class="flow-arrow seg-1" transform="rotate(45)"  d="M-24 -384 H8 V-398 L34 -375 L8 -352 V-366 H-24 Z"/>
    <path class="flow-arrow seg-2" transform="rotate(90)"  d="M-24 -384 H8 V-398 L34 -375 L8 -352 V-366 H-24 Z"/>
    <path class="flow-arrow seg-3" transform="rotate(135)" d="M-24 -384 H8 V-398 L34 -375 L8 -352 V-366 H-24 Z"/>
    <path class="flow-arrow seg-4" transform="rotate(180)" d="M-24 -384 H8 V-398 L34 -375 L8 -352 V-366 H-24 Z"/>
    <path class="flow-arrow seg-5" transform="rotate(225)" d="M-24 -384 H8 V-398 L34 -375 L8 -352 V-366 H-24 Z"/>
    <path class="flow-arrow seg-6" transform="rotate(270)" d="M-24 -384 H8 V-398 L34 -375 L8 -352 V-366 H-24 Z"/>
    <path class="flow-arrow seg-7" transform="rotate(315)" d="M-24 -384 H8 V-398 L34 -375 L8 -352 V-366 H-24 Z"/>
  </g>

  <g class="labels">
    <text class="step-label dark" x="731" y="437">Responsibility</text>
    <text class="step-label dark" x="731" y="481">Fixed</text>

    <text class="step-label dark" x="881" y="574">Management</text>
    <text class="step-label dark" x="881" y="618">&amp; Oversight</text>

    <text class="step-label dark" x="881" y="785">Manning</text>
    <text class="step-label dark" x="881" y="829">the Team</text>

    <text class="step-label dark" x="727" y="977">Training</text>

    <text class="step-label light" x="485" y="956">Professional</text>
    <text class="step-label light" x="485" y="1000">Development</text>

    <text class="step-label light" x="347" y="799">Benefits</text>

    <text class="step-label light" x="347" y="574">Retention</text>
    <text class="step-label light" x="347" y="618">/ Quality of Life</text>

    <text class="step-label light" x="501" y="437">Sustainment</text>
    <text class="step-label light" x="501" y="481">/ Transition</text>
  </g>

  <text class="title" x="650" y="1224">PROGRAM EVALUATION</text>
</svg>
</body>
</html>
```